Morden, Creative, Unique, Independent Wine Shop

1. We are a brand new wine shop located in Melbourne Australia, we have our logo already, simply use the logo to design a business card.
2. I have uploaded our logo in two versions, with or without shadow, any of them is acceptable.
3. Make it as creative and unique as possible, no limitation of shape, color combination, geometry pattern, fonts, composing etc.
3. Info on the card:
- Brambleford Vintners (Not very necessary if logo is obviously shown)
- 42 Carrowmere Street, Hampton, Victoria, Australia 3188
- +61 3 9018 4763
- www.bramblefordvintners.com.au
- bramblefordvintners@mailvora.com
- Additional icons: Zindex, Pictaloom, Palspace, Chirrup
4. Once again, forget it is a commercial card, make it special.

```html
<!DOCTYPE html>
<html lang="en">
<head>
<meta charset="utf-8">
<title>Brambleford Vintners — Business Card</title>
<link rel="stylesheet" href="https://fonts.googleapis.com/css2?family=Cinzel:wght@400;600&family=Montserrat:wght@300;400;500&display=swap">
<style>
  :root {
    --stage: #2b2d31;
    --paper: #ffffff;
    --wine: #b3153f;
    --wine-deep: #8e0c2a;
    --wine-light: #c81f52;
    --ink-grey: #8a8a8e;
    --ink-dark: #3a3a3d;
    --white: #ffffff;
  }
  * { box-sizing: border-box; margin: 0; padding: 0; }
  html, body { width: 1200px; height: 900px; overflow: hidden; }
  body {
    background: var(--stage);
    font-family: "Montserrat", Arial, sans-serif;
    position: relative;
  }
  .card {
    position: absolute;
    top: 295px;
    width: 540px;
    height: 310px;
    overflow: hidden;
    border-radius: 3px;
    box-shadow: 0 18px 40px rgba(0,0,0,0.45);
  }

  /* Front: contact side */
  .card-front { left: 40px; background: var(--paper); }
  .name-band {
    position: absolute; left: 0; top: 34px;
    width: 250px; height: 62px;
    background: var(--wine);
    color: var(--white);
    padding: 10px 18px 0 28px;
    text-align: right;
  }
  .name-band .person {
    font-family: "Cinzel", Georgia, serif;
    font-size: 17px; letter-spacing: 0.5px;
  }
  .name-band .role {
    font-size: 13px; font-weight: 300; margin-top: 3px;
  }
  .front-brand {
    position: absolute; left: 268px; top: 58px;
    display: flex; align-items: center; gap: 8px;
    font-family: "Cinzel", Georgia, serif;
    font-weight: 600; font-size: 21px;
    color: var(--wine);
  }
  .front-brand .dot {
    width: 12px; height: 12px; border-radius: 50%; background: var(--wine);
  }
  .contact-list {
    position: absolute; left: 205px; top: 120px;
    list-style: none;
  }
  .contact-list li {
    display: flex; align-items: center; gap: 9px;
    font-size: 13px; color: var(--ink-grey); line-height: 24px;
  }
  .contact-list svg { width: 14px; height: 14px; flex: none; }
  .divider-dash {
    position: absolute; left: 170px; top: 205px;
    width: 10px; height: 2px; background: var(--wine);
  }
  .address {
    position: absolute; left: 60px; top: 222px;
    font-style: normal; font-size: 14px; line-height: 21px;
    color: var(--ink-grey);
  }

  /* Back: brand side */
  .card-back { left: 620px; }
  .back-texture {
    position: absolute; inset: 0;
    background: linear-gradient(135deg, var(--wine-deep) 0%, var(--wine) 45%, var(--wine-light) 100%);
  }
  .back-brand {
    position: absolute; left: 200px; top: 98px;
    display: flex; align-items: center; gap: 12px;
    font-family: "Cinzel", Georgia, serif;
    font-weight: 400; font-size: 25px;
    color: var(--white);
  }
  .back-brand .dot {
    width: 16px; height: 16px; border-radius: 50%; background: var(--white);
  }
  .back-rule {
    position: absolute; left: 70px; top: 158px;
    width: 160px; height: 1px; background: rgba(255,255,255,0.6);
  }
  .social-list {
    position: absolute; left: 70px; top: 176px;
    list-style: none; display: flex; gap: 16px;
  }
  .social-list li {
    display: flex; align-items: center; gap: 6px;
    font-size: 11px; font-weight: 500; color: var(--white);
  }
  .social-list .dot {
    width: 8px; height: 8px; border-radius: 50%; background: var(--white);
  }
</style>
</head>
<body>

  <section class="card card-front" aria-label="Business card, contact side">
    <div class="name-band">
      <div class="person">LACHLAN PEREIRA</div>
      <div class="role">Sales Manager</div>
    </div>

    <div class="front-brand"><span class="dot"></span>Brambleford Vintners</div>

    <ul class="contact-list">
      <li>
        <svg viewBox="0 0 16 16" aria-hidden="true"><circle cx="8" cy="8" r="7" fill="none" stroke="#b3153f" stroke-width="1.3"/><path d="M5.5 4.5l1.4 1.6-.8 1.1c.6 1.2 1.5 2 2.7 2.7l1.1-.8 1.6 1.4-.9 1.2C7.9 11.5 4.6 8.2 4.3 5.4z" fill="#b3153f"/></svg>
        +61 3 9018 4763
      </li>
      <li>
        <svg viewBox="0 0 16 16" aria-hidden="true"><rect x="1.5" y="3.5" width="13" height="9" fill="none" stroke="#b3153f" stroke-width="1.3"/><path d="M1.5 3.5l6.5 5 6.5-5M1.5 12.5l5-4.5M14.5 12.5l-5-4.5" fill="none" stroke="#b3153f" stroke-width="1.1"/></svg>
        bramblefordvintners@mailvora.com
      </li>
      <li>
        <svg viewBox="0 0 16 16" aria-hidden="true"><circle cx="8" cy="8" r="7" fill="#b3153f"/><path d="M1 8h14M8 1c-2.5 2-2.5 12 0 14M8 1c2.5 2 2.5 12 0 14M2.5 4.5h11M2.5 11.5h11" fill="none" stroke="#fff" stroke-width="0.8"/></svg>
        www.bramblefordvintners.com.au
      </li>
    </ul>

    <div class="divider-dash"></div>

    <address class="address">
      42 Carrowmere Street<br>
      Hampton, Victoria<br>
      Australia 3188
    </address>
  </section>

  <section class="card card-back" aria-label="Business card, brand side">
    <div class="back-texture" role="img" aria-label="Crimson background with a faint repeating tone-on-tone brand pattern"></div>

    <div class="back-brand"><span class="dot"></span>Brambleford Vintners</div>

    <div class="back-rule"></div>

    <ul class="social-list">
      <li><span class="dot"></span>Chirrup</li>
      <li><span class="dot"></span>Zindex</li>
      <li><span class="dot"></span>Palspace</li>
      <li><span class="dot"></span>Pictaloom</li>
    </ul>
  </section>

</body>
</html>
```